Talvex Industrial Maintenance Business Card

Design a business card with the following information, logo must be included.
Talvex Industrial Maintenance
Dale Virnow Jr.
Pone 413-627-8154
email dale.virnow.jr@brindlemail.net

```html
<!DOCTYPE html>
<html lang="en">
<head>
<meta charset="utf-8">
<title>Talvex Industrial Maintenance – Business Card</title>
<link href="https://fonts.googleapis.com/css2?family=Montserrat:wght@600&family=Arimo:wght@400;700&display=swap" rel="stylesheet">
<style>
  :root {
    --backdrop: #b7b7b7;
    --card-white: #ffffff;
    --brand-blue: #0d72b9;
    --accent-blue: #2f96d6;
    --faint-blue: #3479c0;
    --ink: #333333;
    --rule: #333333;
  }
  html, body {
    margin: 0;
    width: 1200px;
    height: 1200px;
    overflow: hidden;
    background: var(--backdrop);
  }
  .card {
    position: absolute;
    left: 189px;
    width: 822px;
    height: 470px;
    overflow: hidden;
    box-shadow: 2px 3px 4px rgba(0,0,0,0.3);
  }
  .card--front { top: 102px; background: var(--card-white); }
  .card--back  { top: 628px; background: var(--brand-blue); }

  .brand {
    position: absolute;
    display: flex;
    align-items: center;
    font-family: "Montserrat", sans-serif;
    font-weight: 600;
  }
  .brand__dot {
    border-radius: 50%;
    box-sizing: border-box;
    flex: none;
  }
  .brand__name { line-height: 1; }
  .brand__name span { display: block; }

  .card--front .brand { left: 95px; top: 200px; color: var(--brand-blue); }
  .card--front .brand__dot { width: 70px; height: 70px; border: 10px solid var(--brand-blue); margin-right: 14px; }
  .card--front .brand__title { font-size: 46px; letter-spacing: 0.5px; }
  .card--front .brand__sub { font-size: 13.2px; margin-top: 3px; }

  .divider {
    position: absolute;
    left: 411px;
    top: 180px;
    width: 2px;
    height: 110px;
    background: var(--rule);
  }
  .contact {
    position: absolute;
    left: 435px;
    top: 180px;
    font-family: "Arimo", Arial, sans-serif;
  }
  .contact__name {
    margin: 0;
    font-size: 29px;
    font-weight: 700;
    color: var(--accent-blue);
    line-height: 1.2;
  }
  .contact__list { list-style: none; margin: 14px 0 0; padding: 0; }
  .contact__item {
    display: flex;
    align-items: center;
    font-size: 21.5px;
    color: var(--ink);
    height: 30px;
  }
  .contact__item svg { width: 18px; height: 18px; margin-right: 14px; flex: none; }

  .backdrop-ring {
    position: absolute;
    left: 80px;
    top: 50px;
    width: 380px;
    height: 380px;
    border-radius: 50%;
    border: 60px solid var(--faint-blue);
    box-sizing: border-box;
  }
  .card--back .brand { left: 178px; top: 174px; color: #ffffff; }
  .card--back .brand__dot { width: 120px; height: 120px; border: 14px solid #ffffff; margin-right: 26px; }
  .card--back .brand__title { font-size: 78px; }
  .card--back .brand__sub { font-size: 21px; margin-top: 4px; }
</style>
</head>
<body>
  <section class="card card--front">
    <div class="brand">
      <div class="brand__dot"></div>
      <div class="brand__name">
        <span class="brand__title">TALVEX</span>
        <span class="brand__sub">INDUSTRIAL MAINTENANCE</span>
      </div>
    </div>
    <div class="divider"></div>
    <div class="contact">
      <h1 class="contact__name">DALE VIRNOW JR.</h1>
      <ul class="contact__list">
        <li class="contact__item">
          <svg viewBox="0 0 24 24" aria-hidden="true"><path fill="#2f96d6" d="M6.6 10.8a15.1 15.1 0 0 0 6.6 6.6l2.2-2.2c.3-.3.7-.4 1-.2 1.1.4 2.3.6 3.6.6.6 0 1 .4 1 1V20c0 .6-.4 1-1 1A17 17 0 0 1 3 4c0-.6.4-1 1-1h3.5c.6 0 1 .4 1 1 0 1.3.2 2.5.6 3.6.1.3 0 .7-.2 1z"/></svg>
          413-627-8154
        </li>
        <li class="contact__item">
          <svg viewBox="0 0 24 24" aria-hidden="true"><rect x="2.5" y="5" width="19" height="14" rx="2" fill="none" stroke="#2f96d6" stroke-width="2"/><path d="M3 6l9 7 9-7" fill="none" stroke="#2f96d6" stroke-width="2"/></svg>
          dale.virnow.jr@brindlemail.net
        </li>
      </ul>
    </div>
  </section>

  <section class="card card--back">
    <div class="backdrop-ring"></div>
    <div class="brand">
      <div class="brand__dot"></div>
      <div class="brand__name">
        <span class="brand__title">TALVEX</span>
        <span class="brand__sub">INDUSTRIAL MAINTENANCE</span>
      </div>
    </div>
  </section>
</body>
</html>
```